Business Card Design Project

Business Card
We are rebranding with a new logo
Industry/Entity Type
Business
Contact Information for Business Card
Doug Farrow +61 457820913 doug@lumora.com.au P.O. Box 728 Kelmscott QLD 4309
Requirements
Must have
- Logo

```html
<!DOCTYPE html>
<html lang="en">
<head>
<meta charset="utf-8">
<title>Lumora International – Business Card</title>
<link rel="stylesheet" href="https://fonts.googleapis.com/css2?family=Hind:wght@500;600&family=Libre+Franklin:wght@300&display=swap">
<style>
  :root {
    --paper-light: #fbfbfb;
    --paper-grey: #e4e5e7;
    --ink: #111111;
    --ink-muted: #9a9a9a;
    --brand-blue: #1a78c8;
    --accent-orange: #ff6a00;
    --accent-orange-deep: #e8540a;
    --wave-cyan: #9ffcfb;
    --wave-teal: #6fb6d4;
    --wave-navy: #3f3f6e;
    --contact-text: #dff8ff;
  }
  html, body {
    margin: 0;
    padding: 0;
    width: 717px;
    height: 1200px;
    overflow: hidden;
    background: #ffffff;
  }
  .card {
    position: relative;
    width: 717px;
    height: 1200px;
    overflow: hidden;
    background:
      radial-gradient(ellipse at 50% 55%, var(--paper-light) 0%, #f2f2f3 45%, var(--paper-grey) 100%);
  }
  .card__texture {
    position: absolute;
    inset: 0 0 auto 0;
    height: 420px;
    background: linear-gradient(160deg, #e3e4e6 0%, #f4f4f5 40%, rgba(250,250,250,0) 100%);
  }
  .card__waves {
    position: absolute;
    inset: 0;
    width: 717px;
    height: 1200px;
  }
  .brand {
    position: absolute;
    left: 0;
    right: 0;
    top: 250px;
    text-align: center;
    font-family: "Hind", sans-serif;
    font-weight: 600;
    color: var(--brand-blue);
  }
  .brand__name {
    display: block;
    font-size: 96px;
    line-height: 1;
    letter-spacing: 2px;
  }
  .brand__tagline {
    display: block;
    margin-top: 22px;
    font-size: 28px;
    letter-spacing: 5px;
  }
  .person {
    position: absolute;
    left: 0;
    right: 0;
    top: 556px;
    text-align: center;
    font-family: "Hind", sans-serif;
  }
  .person__name {
    margin: 0;
    font-size: 46px;
    font-weight: 600;
    line-height: 1;
    letter-spacing: 1px;
    text-transform: uppercase;
  }
  .person__first { color: var(--ink); }
  .person__last { color: var(--ink-muted); }
  .person__title {
    margin: 2px 0 0;
    font-size: 31px;
    font-weight: 500;
    color: var(--brand-blue);
    text-transform: uppercase;
  }
  .contacts {
    position: absolute;
    left: 190px;
    top: 850px;
    margin: 0;
    padding: 0;
    list-style: none;
    font-family: "Libre Franklin", sans-serif;
    font-weight: 300;
    font-size: 27px;
    line-height: 33px;
    color: var(--contact-text);
  }
  .contacts__item {
    display: flex;
    align-items: flex-start;
    margin-bottom: 19px;
  }
  .contacts__icon {
    flex: none;
    width: 40px;
    height: 40px;
    margin-right: 19px;
  }
  .contacts__text { padding-top: 2px; }
</style>
</head>
<body>
<main class="card">
  <div class="card__texture"></div>

  <svg class="card__waves" viewBox="0 0 717 1200" aria-hidden="true">
    <defs>
      <linearGradient id="waveFill" x1="0" y1="0" x2="1" y2="1">
        <stop offset="0" stop-color="var(--wave-cyan)"/>
        <stop offset="0.45" stop-color="var(--wave-teal)"/>
        <stop offset="1" stop-color="var(--wave-navy)"/>
      </linearGradient>
    </defs>
    <path d="M0,690 C70,790 200,805 330,757 C460,707 540,652 640,652 C685,652 717,672 717,672 V1200 H0 Z" fill="url(#waveFill)"/>
    <circle cx="250" cy="1150" r="400" fill="#ffffff" opacity="0.08"/>
    <path d="M0,628 C35,735 160,812 330,757 C190,800 70,780 0,700 Z" fill="var(--accent-orange)"/>
    <path d="M0,660 C50,760 170,805 330,757 C200,793 80,775 0,705 Z" fill="var(--accent-orange-deep)"/>
    <path d="M330,757 C460,707 540,652 640,652 C685,652 717,672 717,672" fill="none" stroke="var(--brand-blue)" stroke-width="5"/>
  </svg>

  <div class="brand">
    <span class="brand__name">Lumora</span>
    <span class="brand__tagline">INTERNATIONAL</span>
  </div>

  <section class="person">
    <h1 class="person__name"><span class="person__first">Doug</span> <span class="person__last">Farrow</span></h1>
    <p class="person__title">Job Title</p>
  </section>

  <ul class="contacts">
    <li class="contacts__item">
      <svg class="contacts__icon" viewBox="0 0 40 40" aria-hidden="true">
        <rect width="40" height="40" rx="6" fill="var(--accent-orange)"/>
        <path d="M12,9 l5,0 l2,7 l-3,2 c1.5,3 3.5,5 6.5,6.5 l2,-3 l7,2 l0,5 c-12,1 -20,-7 -19.5,-19.5 Z" fill="#ffffff"/>
      </svg>
      <span class="contacts__text">+61 457820913</span>
    </li>
    <li class="contacts__item">
      <svg class="contacts__icon" viewBox="0 0 40 40" aria-hidden="true">
        <rect width="40" height="40" rx="6" fill="var(--accent-orange)"/>
        <rect x="6" y="11" width="26" height="18" fill="none" stroke="#ffffff" stroke-width="2"/>
        <path d="M6,11 L19,21 L32,11" fill="none" stroke="#ffffff" stroke-width="2"/>
        <circle cx="31" cy="28" r="5" fill="var(--accent-orange)" stroke="#ffffff" stroke-width="2"/>
      </svg>
      <span class="contacts__text">doug@lumora.com.au</span>
    </li>
    <li class="contacts__item">
      <svg class="contacts__icon" viewBox="0 0 40 40" aria-hidden="true">
        <rect width="40" height="40" rx="6" fill="var(--accent-orange)"/>
        <path d="M11,32 V16 a9,9 0 0 1 18,0 V32 Z" fill="#ffffff"/>
        <rect x="14" y="17" width="12" height="8" fill="var(--accent-orange)"/>
        <path d="M14,17 L20,22 L26,17" fill="none" stroke="#ffffff" stroke-width="1.5"/>
      </svg>
      <span class="contacts__text">P.O. Box 728 Kelmscott<br>QLD 4309</span>
    </li>
  </ul>
</main>
</body>
</html>
```